Neues Design für die Homepage eines Taekwondo-Vereins
Zielgruppe
Der Kampfsportgilde Rheinau ist ein Taekwondo-Verein für die ganze Familie. Trainieren können bei uns Kinder ab 5 Jahren ebenso wie Erwachsene. Wir betreiben Breitensport, es steht für uns also nicht der Wettkampf sondern die persönliche Entwicklung unserer Mitglieder im Vordergrund.
Aufgabenstellung
Wichtig ist uns eine vertikale Menüleiste. Das Menü besteht aus Ober- und Unterpunkten. Bitte berücksichtigen Sie dies bei der Layoutgestaltung. Das Impressum sollte im Footer platziert werden. Außerdem sollte die Möglichkeit der Einbindung von Social Media Buttons gegeben sein.
Das Layout der Seite sollte aufgeräumt, aber dennoch einladend sein. Das Design soll das Interesse des Besuchers wecken und dafür sorgen, dass er sich auf Anhieb wohl fühlt.
Wir hätten gerne auf der Startseite vier Teaserkästen, die jeweils aus einem Bild und Text bestehen.
Großen Wert legen wir auf die Tatsache, dass die Seite responsive ist. Das Layout soll für das CMS Wordpress geeignet sein.

```html
<!DOCTYPE html>
<html lang="de">
<head>
<meta charset="utf-8">
<title>Kampfsportgilde Rheinau – Startseite</title>
<link href="https://fonts.googleapis.com/css2?family=Roboto:wght@300;400;500&display=swap" rel="stylesheet">
<style>
  :root {
    --page-bg: #f0f0f0;
    --card-bg: #ffffff;
    --heading: #4a4a4a;
    --nav: #4d4d4d;
    --body: #8a8a8a;
    --accent: #e2401c;
    --rule: #dddddd;
    --social: #3b5998;
  }
  * { box-sizing: border-box; margin: 0; padding: 0; }
  html, body { width: 1200px; height: 1150px; overflow: hidden; }
  body {
    background: var(--page-bg);
    font-family: "Roboto", Arial, sans-serif;
    color: var(--body);
    position: relative;
  }
  .sidebar {
    position: absolute; left: 244px; top: 13px;
    width: 169px; height: 319px;
    background: var(--card-bg);
    text-align: center;
  }
  .brand {
    height: 99px;
    display: flex; flex-direction: column; align-items: center; justify-content: center;
    gap: 6px;
  }
  .brand-mark {
    width: 38px; height: 38px; border-radius: 50%;
    background: var(--accent);
  }
  .brand-name {
    font-size: 10px; font-weight: 500; color: var(--heading);
    text-transform: uppercase; line-height: 1.3;
  }
  .main-nav {
    margin: 0 auto; width: 112px;
    border-top: 1px solid var(--rule);
    border-bottom: 1px solid var(--rule);
    padding: 6px 0 6px;
    list-style: none;
  }
  .main-nav li {
    height: 22.5px; line-height: 22.5px;
    font-size: 10px; font-weight: 500; color: var(--nav);
  }
  .main-nav li.is-active { color: var(--accent); }
  .social {
    margin-top: 13px;
    display: flex; align-items: center; justify-content: center; gap: 5px;
    font-size: 8px; font-weight: 500; color: var(--nav);
  }
  .social-dot { width: 25px; height: 25px; border-radius: 50%; background: var(--social); }

  .content { position: absolute; left: 425px; top: 13px; width: 531px; }
  .card { background: var(--card-bg); margin-bottom: 12.5px; }
  .hero { padding: 12.5px; height: 319px; }
  .hero-photo {
    width: 100%; height: 294px;
    background: linear-gradient(135deg, #d9b89a 0%, #efe6d8 35%, #f3ede2 60%, #d8b08c 100%);
  }
  .about { height: 115px; padding-top: 13px; text-align: center; }
  .card-title {
    font-size: 12.5px; font-weight: 500; color: var(--heading);
    text-transform: uppercase; line-height: 16px;
  }
  .about p {
    width: 460px; margin: 7px auto 0;
    font-size: 10px; font-weight: 300; line-height: 15px;
  }
  .read-more {
    display: inline-block; margin-top: 7px;
    font-size: 10px; font-weight: 500; color: var(--accent);
    text-transform: uppercase; text-decoration: none;
  }
  .teaser { height: 144px; padding: 12.5px; display: flex; gap: 12.5px; }
  .teaser-photo { width: 200px; height: 119px; flex: none; }
  .teaser-body { flex: 1; }
  .teaser-body .card-title { margin-top: -1px; }
  .teaser-body p {
    margin-top: 7px; height: 75px; overflow: hidden;
    font-size: 10px; font-weight: 300; line-height: 15px;
  }
  .teaser-body .read-more { margin-top: 6px; }
  .photo-kids { background: linear-gradient(135deg, #7aa6bf, #e9e6e0 50%, #3a4d7a); }
  .photo-family { background: linear-gradient(180deg, #b7a27c 0%, #5d7ba6 35%, #e8eaee 65%, #b9bcc2 100%); }
  .photo-sport { background: linear-gradient(180deg, #8fa6c2 0%, #7e9bc2 55%, #d8dbe0 70%, #c6c9ce 100%); }
  .photo-defense { background: linear-gradient(160deg, #8a7a64 0%, #a4947c 40%, #e8e4dd 60%, #c9ab8a 100%); }
  .site-footer {
    height: 37.5px; padding: 0 12.5px;
    display: flex; align-items: center; justify-content: space-between;
    font-size: 10px; font-weight: 400;
  }
</style>
</head>
<body>
  <aside class="sidebar">
    <div class="brand">
      <span class="brand-mark"></span>
      <span class="brand-name">Kampfsportgilde<br>Rheinau</span>
    </div>
    <ul class="main-nav">
      <li class="is-active">Home</li>
      <li>Taekwondo</li>
      <li>Kalender</li>
      <li>Bildergalerie</li>
      <li>Downloads</li>
      <li>Gästebuch</li>
      <li>Links</li>
    </ul>
    <div class="social"><span class="social-dot"></span>Freundeskreis</div>
  </aside>

  <main class="content">
    <section class="card hero">
      <div class="hero-photo" role="img" aria-label="Nahaufnahme eines weißen Taekwondo-Anzugs mit Vereinsaufnäher, Hände zeigen darauf"></div>
    </section>

    <section class="card about">
      <h2 class="card-title">Über Kampfsportgilde Rheinau</h2>
      <p>Der Kampfsportgilde Rheinau wurde 1990 von Sabum (Meister)Bernd Sommer (Träger 6. Dan Taekwondo und 1. Dan Hapkido) gegründet. Seit 1973 ist er im Taekwondosport aktiv, unter anderem als Bundesprüfer, Landeskampfrichter und natürlich Trainer.</p>
      <a class="read-more" href="#">Read more</a>
    </section>

    <article class="card teaser">
      <div class="teaser-photo photo-kids" role="img" aria-label="Kind im Taekwondo-Anzug spielt mit Reifen in der Sporthalle"></div>
      <div class="teaser-body">
        <h3 class="card-title">Training fuer Kinder</h3>
        <p>Lorem Ipsum is simply dummy text of the printing and typesetting industry. Lorem Ipsum has been the industry's standard dummy text ever since the 1500s, when an unknown printer took a galley of type and scrambled it to make a type specimen book. It has survived not only five centuries, but also the leap into electronic typesetting.</p>
        <a class="read-more" href="#">Read more</a>
      </div>
    </article>

    <article class="card teaser">
      <div class="teaser-photo photo-family" role="img" aria-label="Gruppe in Taekwondo-Anzügen trainiert gemeinsam in der Sporthalle"></div>
      <div class="teaser-body">
        <h3 class="card-title">Sport für die ganze Familie</h3>
        <p>Lorem Ipsum is simply dummy text of the printing and typesetting industry. Lorem Ipsum has been the industry's standard dummy text ever since the 1500s, when an unknown printer took a galley of type and scrambled it to make a type specimen book. It has survived not only five centuries, but also the leap into electronic typesetting.</p>
        <a class="read-more" href="#">Read more</a>
      </div>
    </article>

    <article class="card teaser">
      <div class="teaser-photo photo-sport" role="img" aria-label="Vereinsmitglieder beim Dehnen auf dem Hallenboden"></div>
      <div class="teaser-body">
        <h3 class="card-title">Breitensport</h3>
        <p>Lorem Ipsum is simply dummy text of the printing and typesetting industry. Lorem Ipsum has been the industry's standard dummy text ever since the 1500s, when an unknown printer took a galley of type and scrambled it to make a type specimen book. It has survived not only five centuries, but also the leap into electronic typesetting.</p>
        <a class="read-more" href="#">Read more</a>
      </div>
    </article>

    <article class="card teaser">
      <div class="teaser-photo photo-defense" role="img" aria-label="Trittübung mit Pratze zwischen zwei Trainierenden in der Halle"></div>
      <div class="teaser-body">
        <h3 class="card-title">Selbstverteidigung</h3>
        <p>Lorem Ipsum is simply dummy text of the printing and typesetting industry. Lorem Ipsum has been the industry's standard dummy text ever since the 1500s, when an unknown printer took a galley of type and scrambled it to make a type specimen book. It has survived not only five centuries, but also the leap into electronic typesetting.</p>
        <a class="read-more" href="#">Read more</a>
      </div>
    </article>

    <footer class="card site-footer">
      <span>© 2017 Kampfsportgilde Rheinau e.V.</span>
      <span>Impressum</span>
    </footer>
  </main>
</body>
</html>
```